Business card for Property Management consultant

I need a business card for my business LX Vantage - I consult to real estate agents to improve the performance of their Property Management departments (rental houses management). The card needs to be very professional looking, incorporating our logo and my photo plus the line "Develop your Rent Roll to Perform"

Target Market(s)

Real Estate business owners

Industry/Entity Type

Business Consultant

Contact Information for Business Card

Business name - LX Vantage (logo uploaded)
My Name : Marcia Kellaway -
Title : Property Management Consultant

Develop your Rent Roll to perform

Phone : +61 438592716
email : marcia@lxvantage.com.au
website ; www.lxvantage.com.au

Requirements
Must have
• Logo
• My photo
• Very corporate / professional look

```html
<!DOCTYPE html>
<html lang="en">
<head>
<meta charset="utf-8">
<title>LX Vantage – Business Card</title>
<link rel="stylesheet" href="https://fonts.googleapis.com/css2?family=Montserrat:wght@500;600;700&family=Open+Sans:wght@400;600&display=swap">
<style>
  :root {
    --backdrop: #0459a0;
    --card-white: #ffffff;
    --gold: #d4a23c;
    --gold-light: #e6bd62;
    --gold-deep: #b9832a;
    --brand-blue: #4a6cc0;
    --logo-navy: #1d2a4a;
    --text-grey: #5a5f66;
    --text-dark: #2b2f36;
    --photo-warm: #c79a86;
    --photo-blue: #2f55b5;
  }
  * { box-sizing: border-box; margin: 0; padding: 0; }
  html, body {
    width: 1200px; height: 845px; overflow: hidden;
    background: var(--backdrop);
  }
  .canvas {
    width: 1200px; height: 845px;
    display: flex; align-items: center; justify-content: center;
  }
  .card {
    position: relative;
    width: 1000px; height: 610px;
    background: var(--card-white);
    overflow: hidden;
    box-shadow: 0 18px 40px rgba(0,0,0,0.35);
  }
  .card-bands { position: absolute; inset: 0; width: 100%; height: 100%; }
  .portrait {
    position: absolute; left: 200px; top: 250px;
    width: 420px; height: 360px;
    border-radius: 200px 200px 0 0;
    background: linear-gradient(180deg, #6b3a26 0%, var(--photo-warm) 38%, var(--photo-warm) 55%, var(--photo-blue) 72%, var(--photo-blue) 100%);
  }
  .brand {
    position: absolute; left: 100px; top: 150px;
    display: flex; align-items: center; gap: 14px;
  }
  .brand-mark { width: 34px; height: 34px; background: var(--brand-blue); }
  .brand-name {
    font-family: 'Montserrat', sans-serif; font-weight: 700;
    font-size: 46px; color: var(--logo-navy); letter-spacing: 1px;
  }
  .details {
    position: absolute; left: 520px; top: 130px; width: 440px;
  }
  .person-name {
    font-family: 'Montserrat', sans-serif; font-weight: 600;
    font-size: 38px; color: var(--brand-blue);
    text-transform: uppercase; letter-spacing: 1px; line-height: 1.1;
  }
  .name-rule { width: 380px; height: 1px; background: var(--gold); margin: 10px 0 8px; }
  .job-title {
    font-family: 'Open Sans', sans-serif; font-size: 19px; color: var(--text-grey);
  }
  .tagline {
    font-family: 'Montserrat', sans-serif; font-weight: 600;
    font-size: 17px; color: var(--gold); text-transform: uppercase;
    letter-spacing: 0.5px; margin-top: 12px;
  }
  .contact-list { list-style: none; margin-top: 34px; margin-left: 60px; }
  .contact-item {
    display: flex; align-items: center; gap: 22px;
    font-family: 'Open Sans', sans-serif; font-size: 18px; color: var(--text-dark);
    margin-bottom: 16px;
  }
  .contact-icon {
    width: 40px; height: 34px; border-radius: 9px;
    border: 3px solid var(--brand-blue);
    display: flex; align-items: center; justify-content: center;
  }
  .contact-icon svg { width: 18px; height: 18px; }
</style>
</head>
<body>
<main class="canvas">
  <section class="card">
    <svg class="card-bands" viewBox="0 0 1000 610" preserveAspectRatio="none" aria-hidden="true">
      <defs>
        <linearGradient id="goldFill" x1="0" y1="0" x2="1" y2="1">
          <stop offset="0" stop-color="var(--gold-light)"/>
          <stop offset="0.6" stop-color="var(--gold)"/>
          <stop offset="1" stop-color="var(--gold-deep)"/>
        </linearGradient>
      </defs>
      <polygon class="band-top" points="0,0 1000,0 1000,14 300,92 0,30" fill="url(#goldFill)"/>
      <polygon class="band-bottom" points="400,610 860,340 1000,310 1000,610" fill="url(#goldFill)"/>
    </svg>

    <div class="portrait" role="img" aria-label="Portrait photo of Marcia Kellaway"></div>

    <div class="brand">
      <span class="brand-mark"></span>
      <span class="brand-name">LX Vantage</span>
    </div>

    <div class="details">
      <h1 class="person-name">Marcia Kellaway</h1>
      <div class="name-rule"></div>
      <p class="job-title">Property Management Consultant</p>
      <p class="tagline">Develop your Rent Roll to Perform</p>

      <ul class="contact-list">
        <li class="contact-item">
          <span class="contact-icon">
            <svg viewBox="0 0 24 24"><path d="M6.6 10.8a15 15 0 0 0 6.6 6.6l2.2-2.2a1 1 0 0 1 1-.25 11.4 11.4 0 0 0 3.6.57 1 1 0 0 1 1 1V20a1 1 0 0 1-1 1A17 17 0 0 1 3 4a1 1 0 0 1 1-1h3.5a1 1 0 0 1 1 1c0 1.25.2 2.45.57 3.57a1 1 0 0 1-.25 1z" fill="var(--gold)"/></svg>
          </span>
          +61 438592716
        </li>
        <li class="contact-item">
          <span class="contact-icon">
            <svg viewBox="0 0 24 24"><rect x="3" y="5" width="18" height="14" rx="1" fill="var(--gold)"/><path d="M3 6l9 7 9-7" stroke="#fff" stroke-width="1.6" fill="none"/></svg>
          </span>
          marcia@lxvantage.com.au
        </li>
        <li class="contact-item">
          <span class="contact-icon">
            <svg viewBox="0 0 24 24"><circle cx="12" cy="12" r="9" fill="var(--gold)"/><path d="M3 12h18M12 3c3 3 3 15 0 18M12 3c-3 3-3 15 0 18" stroke="#fff" stroke-width="1.4" fill="none"/></svg>
          </span>
          www.lxvantage.com.au
        </li>
      </ul>
    </div>
  </section>
</main>
</body>
</html>
```